Business Card Design

My business is writing crime novels to entertain readers. I write legal thrillers and mysteries. I need a card for publishers, agents, other authors, and media.

Industry/Entity Type

Legal

Contact Information for Business Card

Paul Trenholt
www.trenholtnoir.example
pbtrenholt@mailbox.example
0064 27 5170942

```html
<!DOCTYPE html>
<html lang="en">
<head>
<meta charset="utf-8">
<title>Paul Trenholt — Business Card</title>
<link rel="stylesheet" href="https://fonts.googleapis.com/css2?family=Oswald:wght@500&family=Montserrat:wght@600&display=swap">
<style>
  :root {
    --page-bg: #e8e5e1;
    --card-dark: #0e0e0e;
    --card-mid: #2c2c2c;
    --tape-yellow: #f3e41a;
    --ink-black: #0b0b0b;
    --frame-grey: #3a3a3a;
    --portrait-light: #9a9a9a;
    --portrait-dark: #5c5c5c;
  }
  html, body {
    margin: 0;
    padding: 0;
    width: 1200px;
    height: 1181px;
    overflow: hidden;
    background: var(--page-bg);
  }
  .business-card {
    position: absolute;
    left: 40px;
    top: 268px;
    width: 1120px;
    height: 644px;
    display: block;
  }
  .tape-name {
    font-family: "Oswald", "Arial Narrow", sans-serif;
    font-weight: 500;
    font-size: 86px;
    fill: var(--ink-black);
    text-transform: uppercase;
  }
  .contact-line {
    font-family: "Montserrat", Arial, sans-serif;
    font-weight: 600;
    font-size: 22px;
    fill: var(--tape-yellow);
  }
</style>
</head>
<body>
<svg class="business-card" viewBox="0 0 930 535" xmlns="http://www.w3.org/2000/svg" aria-label="Business card of Paul Trenholt, crime novelist">
  <defs>
    <radialGradient id="card-glow" cx="0.5" cy="0.5" r="0.7">
      <stop offset="0" stop-color="var(--card-mid)"/>
      <stop offset="1" stop-color="var(--card-dark)"/>
    </radialGradient>
    <linearGradient id="portrait-tone" x1="0" y1="0" x2="0" y2="1">
      <stop offset="0" stop-color="var(--portrait-light)"/>
      <stop offset="1" stop-color="var(--portrait-dark)"/>
    </linearGradient>
    <clipPath id="card-edge">
      <rect width="930" height="535"/>
    </clipPath>
  </defs>

  <rect class="card-face" width="930" height="535" fill="url(#card-glow)"/>

  <g class="portrait-block">
    <polygon class="portrait-backing" points="24,73 221,23 284,255 86,305" fill="var(--tape-yellow)"/>
    <rect class="portrait-frame" x="50" y="46" width="210" height="238" fill="var(--frame-grey)"/>
    <rect class="portrait-photo" x="58" y="54" width="194" height="222" fill="url(#portrait-tone)" role="img" aria-label="Portrait photograph of the author"/>
  </g>

  <g class="crime-tape" clip-path="url(#card-edge)">
    <g transform="translate(0 402) rotate(-14.2)">
      <rect class="tape-band" x="-200" y="-46" width="1400" height="92" fill="var(--tape-yellow)"/>
      <text class="tape-name" x="-309" y="36" textLength="450" lengthAdjust="spacingAndGlyphs">Paul Trenholt</text>
      <text class="tape-name" x="243" y="36" textLength="450" lengthAdjust="spacingAndGlyphs">Paul Trenholt</text>
      <text class="tape-name" x="795" y="36" textLength="450" lengthAdjust="spacingAndGlyphs">Paul Trenholt</text>
      <text class="contact-line" x="2" y="84" textLength="905" lengthAdjust="spacingAndGlyphs">0064 27 5170942 ◆ pbtrenholt@mailbox.example ◆ www.trenholtnoir.example</text>
    </g>
  </g>
</svg>
</body>
</html>
```